Full Website and E-Commerce Design. New Business. Selling digital downloads related to the call cen

I am planning to launch a new online company called maplequartzservices.com. This will be a place where people who work in call centres can come and purchase downloadable templates, tool-kits, courseware etc to help them in their jobs. The site will also share the latest information around research, best practices, news in the industry. Essentially a hub for Maple Quartz Services related.

I need someone to build the site for me from scratch (I have only just bought the domain name). Everything from the look and feel of the website (focus on easy to use, clean and sharp graphics, with a bit of fun), highly focused on social media and building a community, full blown e-commerce that allows for memberships/subscriptions/and one off purchase models. If you can also design custom graphics (high quality) that would be even better. Given my research of other companies in this space their websites are very dull that look like knowledge bases. I will want alot of cool visuals that attract the customers in. My initial thinking on colour scheme is bright greens/pinks/yellows etc. Not fluorescent though!

The site will contain alot of documents, templates, presentations, videos, articles, white papers etc. You must have experience in the best way to structure the site in an organised manner so that my customer can find what they need very easily.

The person who takes on this work must be happy to work collaboratively with me. It is also key that when the project is delivered that I am able to maintain alot of it myself in terms of uploading documents, blog updates, adding new products, real-time reports/analytics etc.

Whilst you are designing the website I will be working on the content so I will need your help to understand how I structure my content so that it makes sense for the design.

I will base my choice of designer on levels of experience (I will want to see previous work that you have done). I am not adverse to you using tools like shopify etc. if it meets the overall requirements of the site and adds to the functionality/look and feel.

Target Market(s)

People who work in call centres primarily those that are responsible for managing teams of the call centre itself

Industry/Entity Type

Business

Number of Pages Required

5+ page

Font styles to use
Sans Serif

Colors
33b8a4
34a6d7
886aae
b868aa
e667a6
f04a51
f68e4e
faa54b
ffcf3e

Requirements
Must have
• E-commerce functionality that allows for subscriptions and one-off payments
• Credit card processing and accept wire/bank transfers
• Easy to use layout
• Products sold alone and/or as part of bundles
• Membership area
• Front page
• About Us page
• Contact Us page
• Store page (with e-commerce back end)
• News page
• Free Resources page
• Cool, bright, fun look and feel
Nice to have
• Cool, bright, fun graphics
Should not have
• Should not look old fashioned or be difficult to navigate
• Should not look too busy or disorganised

```html
<!DOCTYPE html>
<html lang="en">
<head>
<meta charset="utf-8">
<title>Maple Quartz Services</title>
<link href="https://fonts.googleapis.com/css2?family=Open+Sans:wght@400;600&display=swap" rel="stylesheet">
<style>
:root{
  --green:#76b82a;
  --purple:#7b3a9a;
  --orange:#eb9a2c;
  --nav-active:#8a3f9c;
  --ink:#2b2b2b;
  --footer:#2a2a2a;
  --line:#3a3a3a;
}
*{margin:0;padding:0;box-sizing:border-box}
html,body{width:1200px;height:888px;overflow:hidden}
body{font-family:"Open Sans",Arial,sans-serif;position:relative;color:var(--ink)}
.backdrop{position:absolute;inset:0;background:
  radial-gradient(ellipse at 80% 30%,#c9b79f 0%,transparent 45%),
  radial-gradient(ellipse at 10% 60%,#8f7a66 0%,transparent 50%),
  linear-gradient(180deg,#7d6f63 0%,#5a4f47 55%,#3e3833 100%)}
.site-header{position:absolute;left:0;top:0;width:1200px;height:104px;background:rgba(240,240,240,.92);border-bottom:1px solid #b9b9b9}
.brand{position:absolute;left:92px;top:38px;display:flex;align-items:center;gap:10px;font-size:24px;font-weight:400;color:var(--green);letter-spacing:.3px}
.brand-mark{width:14px;height:14px;background:var(--green)}
.main-nav{position:absolute;top:66px;left:449px;height:38px}
.main-nav a{position:absolute;top:0;font-size:14px;color:var(--ink);text-decoration:none;letter-spacing:.4px;white-space:nowrap}
.main-nav a.active::after{content:"";position:absolute;left:-8px;right:-4px;top:31px;height:3px;background:var(--nav-active)}
.categories{position:absolute;left:92px;top:161px;width:217px;height:594px;background:rgba(250,250,250,.96)}
.categories h2{height:49px;background:#222;color:#fff;font-weight:400;font-size:20px;padding:12px 0 0 15px;border:1px solid #fff}
.categories ul{list-style:none;padding-top:9px}
.categories li{height:35px;line-height:35px;font-size:13.5px;padding-left:27px;position:relative;letter-spacing:.2px}
.categories li svg{position:absolute;left:11px;top:14px}
.topic-grid{position:absolute;left:334px;top:161px;width:772px;height:594px;background:rgba(25,25,25,.92);display:grid;grid-template-columns:repeat(3,1fr);grid-template-rows:repeat(3,1fr)}
.topic{position:relative;border-right:1px solid var(--line);border-bottom:1px solid var(--line)}
.topic:nth-child(3n){border-right:none}
.topic:nth-child(n+7){border-bottom:none}
.topic-photo{position:absolute;left:10px;top:10px;right:12px;bottom:12px}
.topic-label{position:absolute;left:14px;width:204px;height:49px;line-height:49px;color:#fff;font-weight:600;font-size:13px;letter-spacing:-.3px;padding-left:14px;white-space:nowrap;overflow:hidden}
.row1 .topic-label{top:108px;background:var(--green)}
.row2 .topic-label{top:117px;background:var(--purple)}
.row3 .topic-label{top:118px;background:var(--orange)}
.site-footer{position:absolute;left:91px;top:826px;width:1015px;height:45px;background:rgba(38,38,38,.95);color:#eee;font-size:15.5px;text-align:center;line-height:45px}
</style>
</head>
<body>
<div class="backdrop" role="img" aria-label="Blurred background photo of a warm cafe interior with hanging lamps"></div>

<header class="site-header">
  <div class="brand"><span class="brand-mark"></span>Maple Quartz Services</div>
  <nav class="main-nav">
    <a href="#" class="active" style="left:0">HOME</a>
    <a href="#" style="left:90px">ABOUT US</a>
    <a href="#" style="left:209px">NEWS</a>
    <a href="#" style="left:297px">FREE STUFF</a>
    <a href="#" style="left:423px">MEMBERSHIP</a>
    <a href="#" style="left:564px">CONTACT US</a>
  </nav>
</header>

<aside class="categories">
  <h2>All Categories</h2>
  <ul>
    <li><svg width="8" height="8" viewBox="0 0 8 8"><path d="M0 4h7M4 1l3 3-3 3" stroke="#333" fill="none" stroke-width="1.2"/></svg>Suspendisse pulvinar</li>
    <li><svg width="8" height="8" viewBox="0 0 8 8"><path d="M0 4h7M4 1l3 3-3 3" stroke="#333" fill="none" stroke-width="1.2"/></svg>Fusce quis erat consequat</li>
    <li><svg width="8" height="8" viewBox="0 0 8 8"><path d="M0 4h7M4 1l3 3-3 3" stroke="#333" fill="none" stroke-width="1.2"/></svg>Aliquam convallis</li>
    <li><svg width="8" height="8" viewBox="0 0 8 8"><path d="M0 4h7M4 1l3 3-3 3" stroke="#333" fill="none" stroke-width="1.2"/></svg>Proin lobortis</li>
    <li><svg width="8" height="8" viewBox="0 0 8 8"><path d="M0 4h7M4 1l3 3-3 3" stroke="#333" fill="none" stroke-width="1.2"/></svg>Etiam ac arcu et lacus</li>
    <li><svg width="8" height="8" viewBox="0 0 8 8"><path d="M0 4h7M4 1l3 3-3 3" stroke="#333" fill="none" stroke-width="1.2"/></svg>Nunc sit amet eros</li>
    <li><svg width="8" height="8" viewBox="0 0 8 8"><path d="M0 4h7M4 1l3 3-3 3" stroke="#333" fill="none" stroke-width="1.2"/></svg>Aenean rhoncus</li>
    <li><svg width="8" height="8" viewBox="0 0 8 8"><path d="M0 4h7M4 1l3 3-3 3" stroke="#333" fill="none" stroke-width="1.2"/></svg>Suspendisse pulvinar</li>
    <li><svg width="8" height="8" viewBox="0 0 8 8"><path d="M0 4h7M4 1l3 3-3 3" stroke="#333" fill="none" stroke-width="1.2"/></svg>Fusce quis erat consequat</li>
    <li><svg width="8" height="8" viewBox="0 0 8 8"><path d="M0 4h7M4 1l3 3-3 3" stroke="#333" fill="none" stroke-width="1.2"/></svg>Aliquam convallis</li>
    <li><svg width="8" height="8" viewBox="0 0 8 8"><path d="M0 4h7M4 1l3 3-3 3" stroke="#333" fill="none" stroke-width="1.2"/></svg>Proin lobortis</li>
    <li><svg width="8" height="8" viewBox="0 0 8 8"><path d="M0 4h7M4 1l3 3-3 3" stroke="#333" fill="none" stroke-width="1.2"/></svg>Etiam ac arcu et lacus</li>
    <li><svg width="8" height="8" viewBox="0 0 8 8"><path d="M0 4h7M4 1l3 3-3 3" stroke="#333" fill="none" stroke-width="1.2"/></svg>Nunc sit amet eros</li>
    <li><svg width="8" height="8" viewBox="0 0 8 8"><path d="M0 4h7M4 1l3 3-3 3" stroke="#333" fill="none" stroke-width="1.2"/></svg>Nunc sit amet eros</li>
    <li><svg width="8" height="8" viewBox="0 0 8 8"><path d="M0 4h7M4 1l3 3-3 3" stroke="#333" fill="none" stroke-width="1.2"/></svg>Aenean rhoncus</li>
  </ul>
</aside>

<main class="topic-grid">
  <div class="topic row1">
    <div class="topic-photo" role="img" aria-label="Photo of an office desk with monitors showing charts" style="background:linear-gradient(135deg,#e9edf0,#b9c3c8 60%,#8a8f90)"></div>
    <div class="topic-label">Performance Measurement</div>
  </div>
  <div class="topic row1">
    <div class="topic-photo" role="img" aria-label="Photo of a business team joining hands in a circle" style="background:linear-gradient(135deg,#3a3a3d,#c9c4be 55%,#4a4a4e)"></div>
    <div class="topic-label">Morale and Motivation</div>
  </div>
  <div class="topic row1">
    <div class="topic-photo" role="img" aria-label="Photo of two women in a coaching conversation" style="background:linear-gradient(135deg,#d8cbb6,#a79272 55%,#e8e2d4)"></div>
    <div class="topic-label">Coaching and Mentoring</div>
  </div>
  <div class="topic row2">
    <div class="topic-photo" role="img" aria-label="Photo of a manager listening to a presentation" style="background:linear-gradient(135deg,#eef1f4,#aeb6c0 55%,#3b3e44)"></div>
    <div class="topic-label">Leadership and Management</div>
  </div>
  <div class="topic row2">
    <div class="topic-photo" role="img" aria-label="Photo of a smiling team applauding" style="background:linear-gradient(135deg,#d9c2a8,#efe6dc 50%,#9c8a78)"></div>
    <div class="topic-label">Reward and Recognition</div>
  </div>
  <div class="topic row2">
    <div class="topic-photo" role="img" aria-label="Photo of colleagues talking in a meeting" style="background:linear-gradient(135deg,#f2f2f2,#c8bba9 55%,#6f6a63)"></div>
    <div class="topic-label">Communication Skills</div>
  </div>
  <div class="topic row3">
    <div class="topic-photo" role="img" aria-label="Photo of call centre agents wearing headsets" style="background:linear-gradient(135deg,#f3f3f3,#b9c1c9 55%,#4f5358)"></div>
    <div class="topic-label">Call Centre Technology</div>
  </div>
  <div class="topic row3">
    <div class="topic-photo" role="img" aria-label="Photo of a team planning around a table" style="background:linear-gradient(135deg,#e8e1d4,#8d8172 55%,#3c3a37)"></div>
    <div class="topic-label">Call Centre Strategy</div>
  </div>
  <div class="topic row3">
    <div class="topic-photo" role="img" aria-label="Photo of young people laughing outdoors in sunlight" style="background:linear-gradient(135deg,#f4e2b8,#c89a6a 55%,#6b5a4a)"></div>
    <div class="topic-label">Research and Best Practices</div>
  </div>
</main>

<footer class="site-footer">© 2015 Maplequartzservices. All rights reserved</footer>
</body>
</html>
```